TAVORA MED -DIAGNOSTIC CENTRE FOR IMAGES

Our Activity provides diagnostic services for images (RMI, Tac, RX, Ultrasound etc.)
We would like to create a broschure that illustrates our services.
We would like to give maximum attention to the Diagnostic service dedicated to "HEART", therefore maximum evidence to the world of Cardiology.
In the background we would like to highlight the other diagnostic services dedicated to the Rest of the Body (Brain, Knees Legs etc.)
Target Market(s)
PERSONS WHO NEED TO PERFORM DIAGNOSTIC TESTS (MRI, CT, ULTRASOUND, RX ETC.)
Industry/Entity Type
HEALTH
Requirements
Must have
- The company logo, must have diagnostic images (MRI, CT, X-ray, ultrasound), must be simple and intuitive, which is harmonious with the colors of our company logo
Should not have
- Colours that are not in harmony with our company logo

```html
<!DOCTYPE html>
<html lang="en">
<head>
<meta charset="utf-8">
<title>Tavora Med – Brochure Spread</title>
<link href="https://fonts.googleapis.com/css2?family=Montserrat:wght@400;500;600;700&display=swap" rel="stylesheet">
<style>
  :root{
    --brand-blue:#1f63ad;
    --brand-blue-dark:#17518f;
    --brand-teal:#19a59b;
    --ink:#3b3f45;
    --muted:#6b7079;
    --paper:#ffffff;
    --stage:#b9babd;
  }
  html,body{margin:0;padding:0;overflow:hidden;background:var(--stage);}
  .canvas{position:relative;width:842px;height:1200px;overflow:hidden;background:var(--stage);font-family:"Montserrat",sans-serif;}
  .spread{position:absolute;left:0;top:302px;width:842px;height:595px;display:flex;box-shadow:0 10px 30px rgba(0,0,0,.25);}
  .page{position:relative;width:421px;height:595px;overflow:hidden;background:var(--paper);}
  .page--back{box-shadow:inset -10px 0 14px -10px rgba(0,0,0,.25);}
  .page--front{box-shadow:inset 10px 0 14px -10px rgba(0,0,0,.2);}
  .page__shapes{position:absolute;inset:0;}
  .photo{position:absolute;}

  /* back page */
  .intro{position:absolute;left:24px;right:24px;top:26px;}
  .intro__title{margin:0 0 8px;font-size:10px;font-weight:700;letter-spacing:.5px;color:var(--brand-blue);text-align:center;}
  .intro__text{margin:0;font-size:7px;line-height:1.55;color:var(--muted);text-align:center;}
  .equipment-photo{left:22px;top:168px;width:377px;height:250px;
    background:linear-gradient(135deg,#20313f 0%,#4b5a68 22%,#dfe3e8 45%,#f3f5f7 65%,#cfd6de 100%);
    clip-path:polygon(0 8%,100% 0,100% 88%,0 100%);}
  .contact-block{position:absolute;right:24px;top:452px;text-align:right;font-size:9px;line-height:1.55;color:var(--muted);}
  .contact-block__gap{height:6px;}
  .brand-back{position:absolute;left:28px;top:510px;}
  .brand-back__row{display:flex;align-items:center;gap:6px;}
  .brand-back__name{font-size:21px;font-weight:700;color:var(--brand-blue);letter-spacing:.5px;line-height:1;}
  .brand-back__dot{width:8px;height:8px;border-radius:50%;background:var(--brand-teal);}
  .brand-back__tag{margin-top:4px;font-size:7px;font-weight:600;color:var(--brand-teal);}
  .brand-back__web{margin-top:10px;font-size:10px;color:var(--muted);letter-spacing:.3px;}

  /* front page */
  .brand{position:absolute;left:28px;top:28px;display:flex;align-items:center;gap:6px;}
  .brand__name{font-size:22px;font-weight:700;color:var(--brand-blue);letter-spacing:.5px;line-height:1;}
  .brand__dot{width:8px;height:8px;border-radius:50%;background:var(--brand-teal);}
  .brand__tag{position:absolute;left:40px;top:56px;font-size:7px;font-weight:600;color:var(--brand-teal);}
  .headline{position:absolute;right:16px;top:70px;margin:0;text-align:right;color:var(--paper);font-size:12px;font-weight:600;letter-spacing:.5px;line-height:1.35;}
  .scanner-photo{left:150px;top:128px;width:271px;height:300px;
    background:radial-gradient(circle at 60% 40%,#f4f6f9 0%,#dde3ea 45%,#b9c6d4 70%,#8fc3ec 100%);
    clip-path:polygon(0 0,100% 0,100% 100%,0 100%);}
  .features{position:absolute;left:28px;top:168px;margin:0;padding:0;list-style:none;}
  .features__item{display:flex;align-items:center;gap:5px;margin-bottom:13px;color:var(--paper);font-size:10px;font-weight:500;letter-spacing:.8px;}
  .features__item svg{width:13px;height:10px;}
  .tests{position:absolute;left:24px;top:440px;color:var(--paper);font-size:11.5px;font-weight:600;letter-spacing:.5px;line-height:1.35;}
  .tagline{position:absolute;left:0;right:0;top:504px;margin:0;text-align:center;color:var(--ink);font-size:10.5px;font-weight:600;}
  .contact{position:absolute;left:0;right:0;top:556px;text-align:center;color:var(--paper);font-size:7px;line-height:1.7;font-weight:500;}
</style>
</head>
<body>
<main class="canvas">
  <div class="spread">

    <section class="page page--back">
      <svg class="page__shapes" viewBox="0 0 421 595" width="421" height="595" aria-hidden="true">
        <polygon points="0,150 421,120 421,440 0,440" fill="var(--brand-blue)"/>
        <polygon points="0,150 170,138 150,168 0,180" fill="var(--brand-teal)"/>
        <polygon points="250,395 421,380 421,435 230,440" fill="var(--brand-teal)"/>
        <polygon points="0,440 421,425 421,436 0,452" fill="var(--paper)"/>
      </svg>

      <div class="intro">
        <h2 class="intro__title">TAVORA MED SCAN CENTER LOCATED IN COUNTRY NAME., CITY</h2>
        <p class="intro__text">Our imaging centre offers MRI, CT, ultrasound and X-ray studies with a special focus on cardiology. Experienced radiologists and modern scanners give accurate results quickly. Heart checks, brain scans and studies of knees and legs are booked in one visit, with clear reports sent to you and your doctor.</p>
      </div>

      <div class="photo equipment-photo" role="img" aria-label="Photos of ultrasound unit, X-ray system and CT scanner"></div>

      <div class="contact-block">
        Suite 4, Harbor Lane,<br>NY 0120
        <div class="contact-block__gap"></div>
        123 . 555 01890<br>hello@tavoramed-example.com
      </div>

      <div class="brand-back">
        <div class="brand-back__row"><span class="brand-back__name">TAVORA MED</span><span class="brand-back__dot"></span></div>
        <div class="brand-back__tag">Health Care Diagnostic</div>
        <div class="brand-back__web">www.tavoramed-example.com</div>
      </div>
    </section>

    <section class="page page--front">
      <svg class="page__shapes" viewBox="0 0 421 595" width="421" height="595" aria-hidden="true">
        <polygon points="205,58 421,58 421,122 150,122" fill="var(--brand-teal)"/>
        <polygon points="232,58 421,58 421,122 180,122" fill="var(--brand-blue)"/>
        <polygon points="0,130 421,124 421,428 0,440" fill="var(--brand-blue)"/>
        <polygon points="0,424 352,424 306,486 0,496" fill="var(--brand-teal)"/>
        <polygon points="0,428 340,428 296,480 0,490" fill="var(--brand-blue-dark)"/>
        <polygon points="0,542 421,522 421,595 0,595" fill="var(--brand-teal)"/>
      </svg>

      <div class="photo scanner-photo" role="img" aria-label="Photo of an MRI scanner with patient table"></div>

      <div class="brand"><span class="brand__name">TAVORA MED</span><span class="brand__dot"></span></div>
      <div class="brand__tag">Health Care Diagnostic</div>

      <h1 class="headline">MRI SCAN &amp;<br>IMAGING CENTERS</h1>

      <ul class="features">
        <li class="features__item"><svg viewBox="0 0 26 20"><polyline points="0,12 8,12 11,4 15,18 18,12 26,12" fill="none" stroke="var(--brand-teal)" stroke-width="2"/></svg>EXPERIENCE</li>
        <li class="features__item"><svg viewBox="0 0 26 20"><polyline points="0,12 8,12 11,4 15,18 18,12 26,12" fill="none" stroke="var(--brand-teal)" stroke-width="2"/></svg>QUALITY</li>
        <li class="features__item"><svg viewBox="0 0 26 20"><polyline points="0,12 8,12 11,4 15,18 18,12 26,12" fill="none" stroke="var(--brand-teal)" stroke-width="2"/></svg>TECHNOLOGY</li>
        <li class="features__item"><svg viewBox="0 0 26 20"><polyline points="0,12 8,12 11,4 15,18 18,12 26,12" fill="none" stroke="var(--brand-teal)" stroke-width="2"/></svg>ACCURACY</li>
        <li class="features__item"><svg viewBox="0 0 26 20"><polyline points="0,12 8,12 11,4 15,18 18,12 26,12" fill="none" stroke="var(--brand-teal)" stroke-width="2"/></svg>SERVICE</li>
      </ul>

      <div class="tests">DIAGNOSTIC TESTS<br>(MRI, CT, ULTRASOUND, RX ETC.)</div>

      <p class="tagline">Quick Check-Ups - Assured Solutions at the Diagnostic Center</p>

      <div class="contact">123 . 555 01890 &nbsp;|&nbsp; hello@tavoramed-example.com &nbsp;|&nbsp; www.tavoramed-example.com<br>Suite 4, Harbor Lane, NY 0120</div>
    </section>

  </div>
</main>
</body>
</html>
```